Law firm for traffic law - company portfolio

Company folder with logo and picture on the front. On the back only the imprint in DinA4 format. The following folders are ordered
https://www.falzhaus-kremvel.de/mappe-fuer-din-a4-2teilig-mit-2-laschen-40-farbig-aussseite-bedruck-mit-mattfolie-kaschiert.html#content-view

```html
<!DOCTYPE html>
<html lang="de">
<head>
<meta charset="utf-8">
<title>VERKANZ – Mappe Unfall-Management</title>
<link rel="stylesheet" href="https://fonts.googleapis.com/css2?family=Montserrat:wght@400;500;600;700&family=Roboto+Condensed:wght@700;800&display=swap">
<style>
  :root {
    --navy: #0b3a5c;
    --orange: #f5a12b;
    --white: #ffffff;
    --stage: #c4c4c4;
    --photo-dark: #3e4448;
    --photo-red: #8c2a2c;
    --photo-grey: #8e9499;
  }
  html, body {
    margin: 0;
    padding: 0;
    width: 1200px;
    height: 2462px;
    overflow: hidden;
    background: var(--stage);
  }
  .folder-layout {
    position: absolute;
    left: 0;
    top: 716px;
    width: 1200px;
    height: 1029px;
    display: block;
  }
  .pocket, .flap-band { fill: var(--navy); }
  .logo-panel { fill: var(--white); }
  .brand-name {
    font-family: "Montserrat", sans-serif;
    font-weight: 500;
    letter-spacing: 3px;
  }
  .brand-name--front { fill: var(--navy); font-size: 44px; }
  .brand-name--back { fill: var(--white); font-size: 28px; }
  .contact-heading {
    font-family: "Montserrat", sans-serif;
    font-weight: 700;
    font-size: 14px;
    fill: var(--orange);
  }
  .contact-firm {
    font-family: "Montserrat", sans-serif;
    font-weight: 500;
    font-size: 13.5px;
    fill: var(--orange);
  }
  .contact-line {
    font-family: "Montserrat", sans-serif;
    font-weight: 400;
    font-size: 13px;
    fill: var(--white);
  }
  .contact-icon { fill: var(--orange); }
  .headline {
    font-family: "Roboto Condensed", sans-serif;
    font-weight: 800;
    font-size: 33px;
    fill: var(--orange);
    letter-spacing: 0.5px;
  }
  .subline {
    font-family: "Roboto Condensed", sans-serif;
    font-weight: 700;
    font-size: 19px;
    fill: var(--white);
  }
</style>
</head>
<body>
<svg class="folder-layout" viewBox="95 1620 1055 905" xmlns="http://www.w3.org/2000/svg">
  <defs>
    <linearGradient id="photoTone" x1="0" y1="0" x2="1" y2="0.3">
      <stop offset="0" stop-color="var(--photo-red)"/>
      <stop offset="0.5" stop-color="var(--photo-dark)"/>
      <stop offset="1" stop-color="var(--photo-grey)"/>
    </linearGradient>
  </defs>

  <!-- cover photo across front and back -->
  <rect class="cover-photo" x="143" y="1633" width="958" height="500" fill="url(#photoTone)"
        role="img" aria-label="Foto: beschädigtes rotes Auto nach einem Unfall, daneben sitzt ein erschöpfter Mann im Hemd auf der Straße"/>

  <!-- logo panel on front -->
  <rect class="logo-panel" x="622" y="1633" width="479" height="90"/>
  <text class="brand-name brand-name--front" x="861" y="1694" text-anchor="middle">VERKANZ</text>

  <!-- lower navy band with side flaps -->
  <path class="flap-band" d="M143 2133 H1101 L1143 2155 V2287 L1101 2310 H143 L101 2287 V2155 Z"/>

  <!-- pockets -->
  <path class="pocket" d="M143 2300 H613 Q604 2400 600 2480 Q598 2515 565 2515 H143 Z"/>
  <path class="pocket" d="M631 2300 H1101 V2515 H680 Q647 2515 645 2480 Q641 2400 631 2300 Z"/>

  <!-- back: contact details -->
  <text class="contact-heading" x="168" y="2165">KONTAKTDATEN</text>
  <text class="contact-firm" x="168" y="2188">VERKANZ GbR Kanzlei für Verkehrsrecht</text>

  <g class="contact-list">
    <circle class="contact-icon" cx="175" cy="2206" r="4"/>
    <text class="contact-line" x="184" y="2211">Lindenweg 14, 30159 Hannover</text>
    <path class="contact-icon" d="M171 2222 q1 -3 3 -1 l2 3 q0 2 -1 2 q1 3 4 4 q1 -1 2 -1 l3 2 q1 2 -1 3 q-8 1 -12 -12 z"/>
    <text class="contact-line" x="184" y="2229">+49 511 0 00 12 34</text>
    <rect class="contact-icon" x="170" y="2241" width="10" height="7" rx="1"/>
    <text class="contact-line" x="184" y="2247">+49 511 0 00 12 35</text>
    <rect class="contact-icon" x="170" y="2259" width="10" height="7" rx="1"/>
    <text class="contact-line" x="184" y="2265">info@verkanz.de</text>
    <circle class="contact-icon" cx="175" cy="2279" r="5"/>
    <text class="contact-line" x="184" y="2283">www.verkanz.de</text>
  </g>

  <rect class="contact-emblem" x="480" y="2146" width="82" height="82" rx="6" fill="#1d5a86"
        role="img" aria-label="Kontaktsymbol-Würfel mit Brief, Telefon und E-Mail"/>
  <text class="brand-name brand-name--back" x="510" y="2272" text-anchor="middle">VERKANZ</text>

  <!-- front: headline -->
  <text class="headline" x="861" y="2180" text-anchor="middle">PRODESSIONELLES</text>
  <text class="headline" x="861" y="2220" text-anchor="middle">UNFALL-MANAGEMENT</text>
  <text class="subline" x="861" y="2256" text-anchor="middle">DIE KOMPETENTE ABWICKLUNG IHRES</text>
  <text class="subline" x="861" y="2280" text-anchor="middle">VERKEHRSUNFALLES</text>
</svg>
</body>
</html>
```